New Optometry Practice needs a Business Card

Need a business card for an Optometry practice called 'Marlow Family Eyecare'. I would like to use designs that are friendly, fun and professional. Looking to incorporate glasses (see uploaded image). Not interested in design with an 'eye' in logo. Like green, blue, white as color choices..but open to your ideas. Back of card will be an appointment card as well as provide address, phone and email information.

Industry/Entity Type

Business

Contact Information for Business Card

Marlow Family Eyecare
Dr. Celeste Varga, Optometrist (or O.D.)
4170 S Brackenridge Rd Wenatchee, WA 98802
CMarlowfamilyeyecare.example

Colors
acd036
33b8a4
f68d4e
cfeae6
fee18a
cadf82

Requirements
Must have
• Appointment card on back with date/time of return for next exam

```html
<!DOCTYPE html>
<html lang="en">
<head>
<meta charset="utf-8">
<title>Marlow Family Eyecare – Business Card</title>
<link href="https://fonts.googleapis.com/css2?family=Questrial&display=swap" rel="stylesheet">
<style>
  :root {
    --page: #e9ecec;
    --mint: #cfeae6;
    --mint-deep: #b6d8d2;
    --teal: #1fb39d;
    --teal-dark: #0f8a76;
    --charcoal: #3a3a3a;
    --ink: #1e2a28;
    --grey-light: #dfe3e3;
    --grey: #a9b1b1;
    --yellow: #fee18a;
    --red: #e0322c;
    --white: #ffffff;
  }
  * { box-sizing: border-box; margin: 0; padding: 0; }
  html, body { width: 1200px; height: 800px; overflow: hidden; }
  body {
    background: var(--page);
    font-family: "Questrial", "Century Gothic", sans-serif;
    color: var(--ink);
    display: flex;
    align-items: center;
    justify-content: center;
    gap: 60px;
  }
  .card {
    position: relative;
    width: 520px;
    height: 297px;
    overflow: hidden;
    box-shadow: 0 6px 18px rgba(0,0,0,.18);
  }

  /* Front */
  .card-front { background: linear-gradient(160deg, var(--mint) 0%, var(--mint-deep) 100%); }
  .front-top-band {
    position: absolute; top: 42px; right: 0;
    width: 270px; height: 14px; background: var(--charcoal);
  }
  .front-brand {
    position: absolute; top: 92px; left: 0; right: 0;
    text-align: center;
  }
  .front-brand .brand-name {
    display: inline-flex; align-items: center; gap: 12px;
    font-size: 34px; color: var(--ink); letter-spacing: .5px;
  }
  .brand-dot {
    width: 14px; height: 14px; border-radius: 50%; background: var(--charcoal);
  }
  .front-web {
    margin-top: 6px; font-size: 12px; letter-spacing: 1.5px; text-transform: uppercase;
  }
  .front-mid-band {
    position: absolute; top: 186px; left: 0;
    width: 390px; height: 20px; background: var(--charcoal);
  }
  .front-doctor {
    position: absolute; bottom: 16px; left: 0;
    width: 330px; padding: 6px 18px;
    background: var(--charcoal); color: var(--white);
    font-size: 14px;
  }

  /* Back */
  .card-back { background: var(--white); }
  .back-header {
    position: absolute; top: 0; left: 0; right: 0; height: 40px;
    background: var(--teal);
  }
  .back-sheet {
    position: absolute; top: 40px; left: 0; right: 0; height: 90px;
    background: linear-gradient(180deg, #f3fbfa, var(--mint));
  }
  .back-name {
    position: absolute; top: 46px; right: 40px;
    display: flex; align-items: center; gap: 10px;
    font-size: 21px; color: var(--ink);
  }
  .back-name .brand-dot { width: 10px; height: 10px; background: var(--teal); }
  .contact-list {
    position: absolute; top: 88px; left: 22px;
    list-style: none; font-size: 10.5px; color: var(--ink);
  }
  .contact-list li { display: flex; align-items: center; gap: 8px; margin-bottom: 6px; }
  .contact-icon {
    width: 15px; height: 15px; background: var(--yellow);
    display: flex; align-items: center; justify-content: center;
  }
  .appointment-band {
    position: absolute; top: 150px; left: 0; right: 0; height: 26px;
    background: linear-gradient(90deg, var(--teal-dark) 0%, var(--teal) 40%);
    display: flex; align-items: center; justify-content: center;
    font-size: 20px; color: var(--ink);
  }
  .back-footer {
    position: absolute; top: 176px; left: 0; right: 0; bottom: 0;
    background: linear-gradient(180deg, var(--grey-light), var(--grey));
  }
  .appointment-fields {
    position: absolute; bottom: 44px; left: 28px; right: 28px;
    display: flex; justify-content: space-between;
    font-size: 12px; color: var(--ink); text-transform: uppercase;
  }
  .field { display: flex; align-items: flex-end; gap: 6px; }
  .field-marker {
    width: 0; height: 0; border-top: 4px solid transparent; border-bottom: 4px solid transparent;
    border-left: 8px solid var(--red); align-self: center;
  }
  .field-line { width: 150px; border-bottom: 1px solid var(--charcoal); margin-bottom: 3px; }
</style>
</head>
<body>
  <section class="card card-front" aria-label="Card front">
    <div class="front-top-band"></div>
    <div class="front-brand">
      <div class="brand-name"><span class="brand-dot"></span>Marlow Family Eyecare</div>
      <div class="front-web">CMarlowfamilyeyecare.example</div>
    </div>
    <div class="front-mid-band"></div>
    <div class="front-doctor">Dr. Celeste Varga, Optometrist</div>
  </section>

  <section class="card card-back" aria-label="Card back, appointment">
    <div class="back-header"></div>
    <div class="back-sheet"></div>
    <div class="back-name"><span class="brand-dot"></span>Marlow Family Eyecare</div>
    <ul class="contact-list">
      <li>
        <span class="contact-icon">
          <svg width="11" height="11" viewBox="0 0 12 12"><path d="M1 6 6 1.5 11 6H9.5v4.5h-2.5V8H5v2.5H2.5V6z" fill="#3a3a3a"/></svg>
        </span>
        4170 S Brackenridge Rd Wenatchee, WA 98802
      </li>
      <li>
        <span class="contact-icon">
          <svg width="11" height="11" viewBox="0 0 12 12"><rect x="1" y="2.5" width="10" height="7" fill="#3a3a3a"/><path d="M1 2.5 6 6.5 11 2.5" fill="none" stroke="#fee18a" stroke-width="1"/></svg>
        </span>
        CMarlowfamilyeyecare@mailbox.example
      </li>
      <li>
        <span class="contact-icon">
          <svg width="11" height="11" viewBox="0 0 12 12"><path d="M3 1 5 3.5 4 5c.8 1.4 1.6 2.2 3 3l1.5-1L11 9l-1.5 2C5.5 10.5 1.5 6.5 1 2.5z" fill="#3a3a3a"/></svg>
        </span>
        509-555-0148
      </li>
    </ul>
    <div class="appointment-band">Appointment</div>
    <div class="back-footer"></div>
    <div class="appointment-fields">
      <div class="field"><span class="field-marker"></span>Date<span class="field-line"></span></div>
      <div class="field"><span class="field-marker"></span>Time<span class="field-line"></span></div>
    </div>
  </section>
</body>
</html>
```